Soap Packaging boxes

I need packaging design for my handmade soap. I'm looking for the design that suite my 100% natural range. I need something more classic, vintage, French style look. I don't know how to explain. Please see photos from others soap maker attached. I don't want to copy them but just want to show you what style that I like.

https://www.facebook.com/velmirabloom?ref=hl
please see my Facebook page for my current logo and colour theme.
The size of my soap is 8.5 cm (L) x 6.5 cm (H) x 2.5 cm (D)

Please tell me what you need to know, I'm not really sure what to do here.

Thank you in advance
Kind regards
Orathai K.

Hi all designer, We have 10 more days to complete the project, and I will give you all the feedback in a couple days. I'm waiting for more design to come in, and then will choose the finalists very soon Won't be long, I'll talk to you guys soon Orathai

Target Market(s)

My products are selling to people around the world. I do have 3 ranges of soaps,
1st = natural herbal tea and/or infusion soap for people that have a skin condition.
2nd= a classic creamy bar of soap, for people who love natural handmade soap with natural colorant and scented with pure essential oil, it all about 100% natural.
3rd= A colourful bar of soap, more in to SOAP ART or art in soap thing. charming, fun and amazed every time when I cut the soap, Its come from the same batch but when it cut, each bar will have a unique design on its own. It's scented with skin safe fragrance oil and colouring by cosmetic colour. This rang of soap its for people who love art and fun fact.

Requirements
Must have
• The packaging for each range of soap will be the same for each range but the name of the soap and colour will be changing to suite each type of soap.

```html
<!DOCTYPE html>
<html lang="en">
<head>
<meta charset="utf-8">
<title>Velmira Bloom – Soap Box Dieline</title>
<link rel="stylesheet" href="https://fonts.googleapis.com/css2?family=Cormorant+Garamond:ital,wght@0,700;1,400&family=Montserrat:wght@400;600&display=swap">
<style>
  :root {
    --paper: #ffffff;
    --cut-line: #3a3a3a;
    --teal: #78a4a2;
    --teal-deep: #5f9592;
    --pattern: #a9c9c7;
    --ink: #3f3f3f;
    --tagline: #8fb4b2;
    --tagline-soft: #bcd8d6;
  }
  html, body { margin: 0; padding: 0; overflow: hidden; background: var(--paper); }
  .canvas { display: block; width: 1200px; height: 909px; }
  .cut { fill: var(--paper); stroke: var(--cut-line); stroke-width: 1; }
  .band { fill: var(--teal); stroke: var(--cut-line); stroke-width: 1; }
  .pattern-fill { fill: var(--pattern); }
  .rule { fill: var(--teal); }
  .band-name { font-family: "Cormorant Garamond", serif; font-weight: 700; font-size: 44px; letter-spacing: 2px; fill: var(--paper); }
  .brand-name { font-family: "Cormorant Garamond", serif; font-weight: 700; font-size: 34px; letter-spacing: 1px; fill: var(--teal-deep); }
  .range-name { font-family: "Cormorant Garamond", serif; font-weight: 700; font-size: 27px; fill: var(--tagline); letter-spacing: 0.5px; }
  .range-note { font-family: "Cormorant Garamond", serif; font-style: italic; font-size: 23px; fill: var(--tagline-soft); }
  .ingredients { font-family: "Montserrat", sans-serif; font-size: 13.5px; fill: var(--ink); }
  .ingredients .label { fill: var(--teal-deep); font-weight: 600; }
  .web { font-family: "Montserrat", sans-serif; font-weight: 600; font-size: 13.5px; fill: var(--teal-deep); }
</style>
</head>
<body>
<svg class="canvas" viewBox="0 0 1385 1049" xmlns="http://www.w3.org/2000/svg">

  <!-- top tuck flap -->
  <rect class="cut" x="448" y="115" width="427" height="83"/>

  <!-- back panel -->
  <rect class="cut" x="448" y="198" width="427" height="302"/>
  <rect class="pattern-fill" x="448" y="198" width="55" height="302" role="img" aria-label="Leafy herb sprig pattern"/>
  <rect class="pattern-fill" x="820" y="198" width="55" height="302" role="img" aria-label="Leafy herb sprig pattern"/>
  <rect class="rule" x="504" y="198" width="6" height="302"/>
  <rect class="rule" x="813" y="198" width="6" height="302"/>

  <g class="back-copy" transform="rotate(180 661.5 349)">
    <text class="ingredients">
      <tspan x="533" y="221"><tspan class="label">Contains:</tspan> Aloe Leaf Juice, Apricot</tspan>
      <tspan x="533" y="240">Kernel Oil, Glycerin, Shea Nut Butter,</tspan>
      <tspan x="533" y="259">Cetearyl Glucoside Beewax,</tspan>
      <tspan x="533" y="278">Macadamia Oil, Sorbitan Olivate,</tspan>
      <tspan x="533" y="297">Radish Root Ferment Filtrate, Camellia</tspan>
      <tspan x="533" y="316">Oil, Sambucus Nigra Fruit Extract,</tspan>
      <tspan x="533" y="335">Xanthan Gum, Calendula Extract,</tspan>
      <tspan x="533" y="354">Potassium Sorbate, Citric Acid, Lactic</tspan>
      <tspan x="533" y="373">Acid, Citrus Limon, Citrus Aurantifolia,</tspan>
      <tspan x="533" y="392">Citrus Paradisi, Pelargonium Asperum.</tspan>
      <tspan x="533" y="430">For external use only.</tspan>
    </text>
    <text class="web" x="533" y="467">www.velmirabloom.com.au</text>
  </g>

  <!-- upper band with side dust flaps -->
  <polygon class="cut" points="448,500 385,500 365,520 365,563 385,583 448,583"/>
  <polygon class="cut" points="875,500 938,500 958,520 958,563 938,583 875,583"/>
  <rect class="band" x="448" y="500" width="427" height="83"/>
  <text class="band-name" x="661.5" y="555" text-anchor="middle" transform="rotate(180 661.5 541)">VELMIRA BLOOM</text>

  <!-- side panels and glue flaps -->
  <polygon class="cut" points="365,583 335,583 315,603 315,865 335,885 365,885"/>
  <polygon class="cut" points="958,583 988,583 1008,603 1008,865 988,885 958,885"/>
  <rect class="pattern-fill" x="365" y="583" width="83" height="302" role="img" aria-label="Leafy herb sprig pattern"/>
  <rect class="pattern-fill" x="875" y="583" width="83" height="302" role="img" aria-label="Leafy herb sprig pattern"/>
  <rect x="365" y="583" width="593" height="302" fill="none" stroke="var(--cut-line)" stroke-width="1"/>

  <!-- front panel -->
  <rect class="cut" x="448" y="583" width="427" height="302"/>
  <rect class="pattern-fill" x="448" y="583" width="55" height="302" role="img" aria-label="Leafy herb sprig pattern"/>
  <rect class="pattern-fill" x="820" y="583" width="55" height="302" role="img" aria-label="Leafy herb sprig pattern"/>
  <rect class="rule" x="504" y="583" width="6" height="302"/>
  <rect class="rule" x="813" y="583" width="6" height="302"/>

  <text class="brand-name" x="661" y="714" text-anchor="middle">VELMIRA BLOOM</text>

  <text class="range-name" x="661" y="846" text-anchor="middle">Natural herbal tea</text>
  <text class="range-note" x="661" y="869" text-anchor="middle">100% natural</text>

  <!-- lower band with side dust flaps -->
  <polygon class="cut" points="448,885 385,885 365,905 365,950 385,970 448,970"/>
  <polygon class="cut" points="875,885 938,885 958,905 958,950 938,970 875,970"/>
  <rect class="band" x="448" y="885" width="427" height="85"/>
  <text class="band-name" x="661.5" y="942" text-anchor="middle">VELMIRA BLOOM</text>
</svg>
</body>
</html>
```